Business Card for Coach - ready to print

Design Business Card ready to order prints www.larsholm.coach

* An Overview / Background of the Business & Services
· Coaching
· Personal growth
* The Target Market / Audience you are trying to reach
· private person in different roles (self, familiy, business role)s
* Design Specifics; any preferences or ideas for Style, Colour, Imagery, etc
· See www.larsholm.coach
· "simple" design
· (small) element of surprise / unusual element

* Information that will be placed in the Business Card
· Beratung und Coaching
· Address: Lars Holm, Kesselgasse 7, CH-8517 Winterthur, Mobile +41 76 254 60 31
* Do you have an existing website or Facebook page where designers can learn more about your company?
· larsholm.coach

Target Market(s)

private person in different roles (self, familiy, business role)

Industry/Entity Type

Life Coaching

Contact Information for Business Card

Lars Holm
Kesselgasse 7
CH-8517 Winterthur

Mobile: +41 76 254 60 31
Email: laho@mailvale.ch
www.larsholm.coach

Font styles to use
Sans Serif

Colors

Designer to choose colors to be used in the design.

Requirements
Must have
• "simple" design
• element of surprise / unusual element
• Beratung & Coaching
• see www.larsholm.coach for colors and so...
Nice to have
• TA Symbol (three rings on top of each other) - unsual presentation
• QR Code of Website (see if it fits in and still looks good).

```html
<!DOCTYPE html>
<html lang="de">
<head>
<meta charset="utf-8">
<title>Lars Holm – Visitenkarte</title>
<link rel="stylesheet" href="https://fonts.googleapis.com/css2?family=Open+Sans:ital,wght@0,600;0,700;1,600&display=swap">
<style>
  :root {
    --backdrop: #dcdbdb;
    --card: #f1f1f1;
    --sky: #a1d5eb;
    --ink: #131313;
  }
  * { margin: 0; padding: 0; box-sizing: border-box; }
  html, body { width: 1200px; height: 1000px; overflow: hidden; }
  body {
    position: relative;
    background: var(--backdrop);
    font-family: "Open Sans", Arial, sans-serif;
    color: var(--ink);
  }
  .card { position: absolute; background: var(--card); }
  .card-front { left: 297px; top: 112px; width: 605px; height: 346px; }
  .card-back  { left: 297px; top: 515px; width: 608px; height: 347px; }
  .card-shapes { position: absolute; inset: 0; width: 100%; height: 100%; }
  .shape-band { fill: var(--sky); }
  .shape-corner { fill: var(--ink); }
  .identity {
    position: absolute; left: 0; right: 0; top: 136px;
    text-align: center;
  }
  .identity-name {
    font-weight: 700; font-size: 41px; line-height: 48px; letter-spacing: 0.2px;
  }
  .identity-role {
    font-weight: 600; font-style: italic; font-size: 17.5px; line-height: 22px;
  }
  .contact {
    position: absolute; left: 0; right: 0; top: 117px;
    text-align: center; font-weight: 600; font-size: 22.5px; line-height: 44px;
  }
  .contact-highlight {
    display: inline-block; background: var(--sky);
    padding: 0 6px; line-height: 29px; margin: 7px 0 8px;
    vertical-align: middle;
  }
  .contact-line { display: block; }
</style>
</head>
<body>
  <section class="card card-front">
    <svg class="card-shapes" viewBox="0 0 605 346" aria-hidden="true">
      <polygon class="shape-band" points="239,21 584,21 584,140 365,324 21,324 21,206"/>
      <polygon class="shape-corner" points="21,21 216,21 21,135"/>
      <polygon class="shape-corner" points="584,210 584,324 389,324"/>
    </svg>
    <div class="identity">
      <h1 class="identity-name">Lars Holm</h1>
      <p class="identity-role">Beratung und Coaching</p>
    </div>
  </section>

  <section class="card card-back">
    <div class="contact">
      <span class="contact-line">kesselgasse 7 ch-8517 winterthur</span>
      <span class="contact-highlight">+41 76 254 60 31 &nbsp;|&nbsp; laho@mailvale.ch</span>
      <span class="contact-line">www.larsholm.coach</span>
    </div>
  </section>
</body>
</html>
```